Asphalt Paving Specialists Business Cards

Our company is TREVIN ASPHALT. We need a business cards two of our asphalt paving team members. We're asphalt specialists.
I need two made up please. The details on the front of the each business card i would like please is as follows.
Address is 87 Marrowby St, Kelvale, QLD, 4087.

Company Director
Gordon Pelliway
gord@trevinpave.com.au
04 58 736 042
www.trevinpave.com.au

Supervisor
Curtis Vonnegard
curtis@trevinpave.com.au
0462 873 105
www.trevinpave.com.au

We do all aspects of Asphalt Paving. Specific Services include - Driveways, Carparks & sub-divisions. All Roads. Repairs and Maintenance.

We provide free quotes!

I dont have a certain way i want them to look so im open to all designs :)

** I have uploaded our logo for the TREVIN ASPHALT. HOWEVER, CAN YOU PLEASE GET RID OF THE ( PTY LTD )

Thank you
Renata Fulch
TREVIN ASPHALT

Target Market(s)

Home owners and Business Owners

Contact Information for Business Card

Asphalt Paving Specialists. All aspects of Asphalt. Residential, Commercial & Industrial. Based in Brisbane.

Font styles to use
Sans Serif

Colors

Designer to choose colors to be used in the design.

Requirements
Nice to have
• maybe an image of a driveway? or Asphalt?

```html
<!DOCTYPE html>
<html lang="en">
<head>
<meta charset="utf-8">
<title>Trevin Asphalt – Business Cards</title>
<link rel="stylesheet" href="https://fonts.googleapis.com/css2?family=Lato:wght@300;400;700&family=Oswald:wght@700&display=swap">
<style>
  :root {
    --backdrop: #3b3430;
    --card: #141414;
    --card-edge: #1d1d1d;
    --brand-blue: #3fb3e6;
    --text-white: #f2f2f2;
    --text-grey: #a8a8a8;
    --rule: #4a4a4a;
  }
  * { margin: 0; padding: 0; box-sizing: border-box; }
  html, body {
    width: 1200px; height: 844px; overflow: hidden;
    background: var(--backdrop);
    font-family: "Lato", Arial, sans-serif;
  }
  .canvas { position: relative; width: 1200px; height: 844px; }
  .card {
    position: absolute; top: 272px;
    width: 520px; height: 300px;
    background: linear-gradient(160deg, var(--card-edge), var(--card));
    box-shadow: 0 14px 30px rgba(0,0,0,.45);
    color: var(--text-white);
  }
  .card--front { left: 60px; }
  .card--back { left: 620px; }

  .brand {
    display: flex; align-items: center; gap: 10px;
    font-weight: 700; font-size: 30px; letter-spacing: 1px;
    color: var(--brand-blue); white-space: nowrap;
  }
  .brand__dot {
    width: 22px; height: 22px; border-radius: 50%;
    background: var(--brand-blue); flex: none;
  }

  .card--front .brand { position: absolute; left: 150px; top: 70px; }
  .card--front .divider {
    position: absolute; left: 32px; right: 32px; top: 152px;
    height: 1px; background: var(--rule);
  }
  .person { position: absolute; left: 32px; top: 168px; }
  .person__name {
    font-size: 21px; font-weight: 400; letter-spacing: .5px;
    color: var(--brand-blue); text-transform: uppercase; white-space: nowrap;
  }
  .person__role { font-size: 15px; color: var(--text-grey); margin-top: 1px; }
  .contact { list-style: none; margin-top: 12px; }
  .contact li {
    display: flex; align-items: center; gap: 8px;
    font-size: 15px; color: var(--text-grey); line-height: 21px; white-space: nowrap;
  }
  .contact svg { width: 12px; height: 12px; fill: var(--brand-blue); flex: none; }
  .address {
    position: absolute; right: 32px; top: 170px;
    text-align: right; font-size: 15px; line-height: 21px;
    color: var(--text-grey); font-style: normal; white-space: nowrap;
  }

  .card--back .brand { justify-content: center; margin-top: 62px; }
  .card--back .divider {
    height: 1px; background: var(--rule); margin: 22px 70px 0 180px;
  }
  .headline {
    font-family: "Oswald", Impact, sans-serif;
    font-size: 21px; text-align: center; margin-top: 14px; letter-spacing: .3px;
    white-space: nowrap;
  }
  .services {
    text-align: center; font-size: 13px; line-height: 18px;
    color: var(--text-grey); margin-top: 6px;
  }
  .quotes {
    display: flex; align-items: center; gap: 10px;
    margin: 6px 60px 0; font-size: 12px; font-weight: 700; white-space: nowrap;
  }
  .quotes::before, .quotes::after {
    content: ""; flex: 1; height: 1px; background: var(--rule);
  }
</style>
</head>
<body>
<main class="canvas">

  <section class="card card--front" aria-label="Business card front">
    <div class="brand"><span class="brand__dot"></span>TREVIN ASPHALT</div>
    <div class="divider"></div>
    <div class="person">
      <p class="person__name">Gordon Pelliway</p>
      <p class="person__role">Company Director</p>
      <ul class="contact">
        <li><svg viewBox="0 0 12 12"><path d="M2 1h3l1 3-1.5 1a7 7 0 0 0 2.5 2.5L8 6l3 1v3c0 .6-.4 1-1 1A9 9 0 0 1 1 2c0-.6.4-1 1-1z"/></svg>04 58 736 042</li>
        <li><svg viewBox="0 0 12 12"><path d="M0 2h12v8H0z M1 3l5 3.5L11 3" stroke="#141414" stroke-width="1"/></svg>gord@trevinpave.com.au</li>
        <li><svg viewBox="0 0 12 12"><circle cx="6" cy="6" r="6"/></svg>www.trevinpave.com.au</li>
      </ul>
    </div>
    <address class="address">87 Marrowby St<br>Kelvale, QLD, 4087</address>
  </section>

  <section class="card card--back" aria-label="Business card back">
    <div class="brand"><span class="brand__dot"></span>TREVIN ASPHALT</div>
    <div class="divider"></div>
    <h2 class="headline">WE DO ALL ASPECTS OF ASPHALT PAVING.</h2>
    <p class="services">Specific Services include - Driveways, Carparks &amp; sub-divisions.<br>All Roads, Repairs and Maintenance.</p>
    <p class="quotes">WE PROVIDE FREE QUOTES!</p>
  </section>

</main>
</body>
</html>
```